Business Card Design - R.T. Custom Cabinets Ltd.

Design a business card, including a new logo for a new company in Vancouver, British Columbia, Canada.

The logo must be available as a separate file.

The card should include all company information including:
R.T. Custom Cabinets Ltd.
2786 Larchmoor Crescent
Burnaby, B.C. V7K 2P9
Telehone: 604-XXX-XXXX
Fax: 604-XXX-XXXX
www.rtcustomcabinets.example

As well as individual contact information for employees:
Name
Position
Telephone
Email

The card must include a thoughtful message as well

Target Market(s)

Custom Cabinets

Industry/Entity Type

Business

Contact Information for Business Card

Important information on the front, thoughtful message on the back

Colors
fbed22
9bcb3c
0355a3
ec1f27

Requirements
Must have
• See project description
Nice to have
• images that showcase custom cabinets (european, modern and traditional) styles

```html
<!DOCTYPE html>
<html lang="en">
<head>
<meta charset="utf-8">
<title>R.T. Custom Cabinets Ltd. – Business Card</title>
<link href="https://fonts.googleapis.com/css2?family=Lato:wght@400;700;900&family=Roboto+Condensed:wght@400&display=swap" rel="stylesheet">
<style>
  :root {
    --brand-blue: #0f55a3;
    --brand-green: #9bcb3c;
    --card-white: #ffffff;
    --backdrop: #3a2418;
    --text-light: #ffffff;
  }
  * { box-sizing: border-box; margin: 0; padding: 0; }
  html, body { width: 1200px; height: 1000px; overflow: hidden; }
  body {
    background: var(--backdrop);
    position: relative;
    font-family: "Lato", Arial, sans-serif;
  }
  .card {
    position: absolute;
    width: 560px;
    height: 320px;
    border-radius: 24px;
    overflow: hidden;
    box-shadow: 0 8px 18px rgba(0,0,0,0.45);
  }
  .card-front { left: 130px; top: 150px; background: var(--card-white); }
  .card-back  { left: 510px; top: 530px; background: var(--brand-blue); }

  .front-bands { position: absolute; inset: 0; }

  .company-mark {
    position: absolute;
    top: 38px;
    right: 34px;
    display: flex;
    align-items: center;
    gap: 14px;
  }
  .mark-square {
    width: 30px; height: 30px;
    background: var(--brand-blue);
  }
  .company-name {
    font-family: "Roboto Condensed", Arial, sans-serif;
    font-weight: 400;
    font-size: 28px;
    line-height: 1.05;
    color: var(--brand-blue);
    text-transform: uppercase;
    letter-spacing: 0.5px;
  }

  .address {
    position: absolute;
    right: 30px;
    top: 134px;
    text-align: right;
    color: var(--text-light);
    font-size: 13px;
    line-height: 1.3;
    font-style: normal;
  }

  .person {
    position: absolute;
    left: 34px;
    top: 194px;
    color: var(--text-light);
  }
  .person-name {
    font-weight: 900;
    font-size: 24px;
    line-height: 1;
  }
  .person-name .surname { color: var(--brand-green); }
  .person-role { font-size: 14px; margin-top: 2px; }

  .contact-list {
    position: absolute;
    left: 34px;
    top: 244px;
    list-style: none;
    color: var(--text-light);
    font-size: 12.5px;
    line-height: 1.4;
  }
  .contact-list li { display: flex; align-items: center; gap: 7px; }
  .contact-list svg { width: 12px; height: 12px; fill: var(--brand-green); flex: none; }

  .back-mark {
    position: absolute;
    inset: 0;
    display: flex;
    align-items: center;
    justify-content: center;
    gap: 16px;
  }
  .back-mark .mark-square { background: var(--card-white); width: 40px; height: 40px; }
  .back-mark .company-name { color: var(--text-light); font-size: 38px; }
</style>
</head>
<body>

<section class="card card-front" aria-label="Business card front">
  <svg class="front-bands" viewBox="0 0 560 320" width="560" height="320" aria-hidden="true">
    <polygon points="0,170 48,170 62,186 76,170 560,118 560,320 0,320" fill="var(--brand-blue)"/>
    <polyline points="0,163 48,163 62,179 76,163 560,111" fill="none" stroke="var(--brand-green)" stroke-width="7"/>
  </svg>

  <div class="company-mark">
    <span class="mark-square"></span>
    <span class="company-name">R.T. Custom<br>Cabinets Ltd.</span>
  </div>

  <address class="address">
    48 Fernbrook Lane<br>
    Westbury<br>
    BC V7K 2P9
  </address>

  <div class="person">
    <p class="person-name">JOHN <span class="surname">DOE</span></p>
    <p class="person-role">Manager</p>
  </div>

  <ul class="contact-list">
    <li>
      <svg viewBox="0 0 24 24"><path d="M6.6 10.8a15.1 15.1 0 0 0 6.6 6.6l2.2-2.2c.3-.3.7-.4 1-.2 1.1.4 2.3.6 3.6.6.6 0 1 .4 1 1V20c0 .6-.4 1-1 1A17 17 0 0 1 3 4c0-.6.4-1 1-1h3.5c.6 0 1 .4 1 1 0 1.3.2 2.5.6 3.6.1.3 0 .7-.2 1z"/></svg>
      604 - 555 - 0142
    </li>
    <li>
      <svg viewBox="0 0 24 24"><circle cx="12" cy="12" r="10" fill="none" stroke="#9bcb3c" stroke-width="2.4"/><path d="M2 12h20M12 2c3 3 3 17 0 20M12 2c-3 3-3 17 0 20" fill="none" stroke="#9bcb3c" stroke-width="2"/></svg>
      www.rtcustomcabinets.example
    </li>
    <li>
      <svg viewBox="0 0 24 24"><rect x="2" y="5" width="20" height="14" rx="1"/><path d="M2 6l10 7 10-7" fill="none" stroke="#0f55a3" stroke-width="2"/></svg>
      jdoe@rtcustomcabinets.example
    </li>
  </ul>
</section>

<section class="card card-back" aria-label="Business card back">
  <div class="back-mark">
    <span class="mark-square"></span>
    <span class="company-name">R.T. Custom Cabinets Ltd.</span>
  </div>
</section>

</body>
</html>
```